Stylish High End Wedding Videography/Films Website (BDMR)

We need a modern and high-end website look for our wedding video and films business. We films weddings all over the United Kingdom and at European destinations so need something to reflect our work. The website should be visually stunning with images and videos being the focal point as this is what our services are;

I have uploads of some items I like and the features the site needs to have. These have been taken from other websites using standout features.

We need the following pages;

1 - Homepage
2 - Films Index Page
3 - Individual Films Page
4 - Prices / Collection Page
5 - Reviews
6 - Options
7 - About
8 - Contact
9 - Blog Index
10 - Blog Page

All pages must be consistent so have a similar style.

Pages on menu:
Films
Prices
Reviews
Options
About
Contact

We require a responsive look too. Over 90% of our visitors access the website via their mobile devices.

Please use the colours from our logo to incorporate into the website.

Target Market(s)

Wedding Couples

Industry/Entity Type

Wedding Photography

Number of Pages Required

5+ page

Font styles to use
Sans Serif
Script

Requirements
Must have
• The logo must be in the centre of the menu at the top.

Social icons at the bottom of the page.

Use only two fonts including Lore which is supplied
Nice to have
• Different video for each page on the top header. This will play behind the menu.

```html
<!DOCTYPE html>
<html lang="en">
<head>
<meta charset="utf-8">
<title>BDMR Wedding Films</title>
<link href="https://fonts.googleapis.com/css2?family=Open+Sans:wght@300;400;600&family=Parisienne&display=swap" rel="stylesheet">
<style>
:root{
  --gold:#a8914f;
  --gold-dark:#8e7a3f;
  --gold-soft:#cdb98a;
  --ink:#3f3f3f;
  --muted:#555;
  --white:#fff;
  --night:#0b0f0d;
  --sand:#ece6df;
  --badge:#f2e77c;
}
*{box-sizing:border-box;margin:0;padding:0}
html,body{width:1200px;height:3548px;overflow:hidden}
body{position:relative;background:var(--white);font-family:"Open Sans",sans-serif;color:var(--ink)}
.abs{position:absolute}
.script{font-family:"Parisienne",cursive;font-weight:400}

/* header */
.site-header{left:0;top:0;width:1200px;height:113px;background:var(--white)}
.nav-link{top:56px;font-size:14px;line-height:20px;color:#222;text-decoration:none}
.brand-mark{left:589px;top:12px;width:22px;height:22px;border:2px solid var(--gold)}
.brand{left:500px;top:54px;width:200px;text-align:center;color:var(--gold-dark);font-size:18px;line-height:24px;letter-spacing:7px}

/* hero */
.hero{left:0;top:113px;width:1200px;height:599px;
  background:
    radial-gradient(ellipse 150px 230px at 870px 480px,rgba(235,238,248,.85),rgba(160,170,195,.35) 55%,rgba(0,0,0,0) 100%),
    radial-gradient(ellipse 110px 90px at 850px 600px,rgba(200,210,235,.55),rgba(0,0,0,0) 100%),
    radial-gradient(ellipse 60px 80px at 780px 470px,rgba(255,230,170,.75),rgba(220,170,80,.3) 55%,rgba(0,0,0,0) 100%),
    radial-gradient(ellipse 55px 260px at 745px 150px,rgba(214,150,40,.8),rgba(140,90,20,.35) 55%,rgba(0,0,0,0) 100%),
    radial-gradient(ellipse 160px 70px at 720px 640px,rgba(90,110,160,.45),rgba(0,0,0,0) 100%),
    linear-gradient(180deg,#0e1412,#070908)}
.hero-title{left:158px;top:314px;font-size:52px;line-height:64px;color:var(--white)}
.hero-sub{left:148px;top:388px;font-size:35px;line-height:46px;font-weight:300;color:var(--white)}
.btn-explore{left:288px;top:456px;width:150px;height:43px;background:var(--gold);color:var(--white);
  font-size:12px;font-weight:600;display:flex;align-items:center;justify-content:center}

/* services */
.section-title{width:1200px;left:0;text-align:center;color:var(--gold);font-size:36px;line-height:48px}
.tile{overflow:hidden}
.tile-band{position:absolute;left:0;right:0;height:50px;top:50%;margin-top:-25px;background:rgba(215,215,215,.55);
  display:flex;align-items:center;justify-content:center;font-family:"Parisienne",cursive;font-size:21px;color:#4a4a4a}

/* about */
.hello{left:149px;top:1786px;font-size:36px;line-height:54px;color:var(--gold)}
.about-text{left:150px;top:1905px;width:420px;font-size:15px;line-height:37.5px;color:var(--muted)}
.btn-outline{left:149px;top:2104px;width:152px;height:47px;border:2px solid var(--gold);color:var(--gold);
  font-size:12px;font-weight:600;display:flex;align-items:center;justify-content:center}
.about-frame{left:583px;top:1785px;width:441px;height:440px;border:2px solid var(--gold)}
.about-photo{left:616px;top:1758px;width:435px;height:434px;
  background:
    radial-gradient(ellipse 90px 80px at 52% 36%,#151515,rgba(21,21,21,.6) 60%,rgba(0,0,0,0)),
    radial-gradient(ellipse 120px 140px at 48% 58%,rgba(150,110,95,.75),rgba(0,0,0,0) 100%),
    radial-gradient(ellipse 70px 120px at 10% 85%,rgba(60,40,30,.7),rgba(0,0,0,0)),
    linear-gradient(160deg,#4a4d52,#6c6a66 40%,#7d8794 75%,#5d6b7c)}

/* reviews */
.cell{width:225px;height:397px}
.quote{padding:16px 7px 10px 7px;font-size:13.5px;line-height:22.5px;color:var(--muted)}
.quote-name{position:absolute;left:7px;bottom:12px;font-size:13.5px;line-height:22.5px;color:var(--gold);font-weight:600}

/* footer */
.footer{left:0;top:3277px;width:1200px;height:231px;background:var(--sand)}
.foot-mark{left:198px;top:3296px;width:14px;height:14px;border:2px solid var(--gold)}
.foot-brand{left:150px;top:3314px;font-size:13px;line-height:18px;letter-spacing:5px;color:var(--gold-dark)}
.foot-text{font-size:12.5px;line-height:18px;color:#4a4a4a}
.foot-small{font-size:11px;line-height:16px;color:#555}
.foot-head{font-size:12px;line-height:18px;font-weight:600;color:#333}
.social{width:38px;height:38px;border-radius:50%;background:var(--gold-soft)}
.badge{left:857px;top:3400px;width:88px;height:88px;border-radius:50%;background:var(--badge)}
.legal{left:0;top:3508px;width:1200px;height:40px;background:var(--gold);color:var(--white);
  font-size:10.5px;display:flex;align-items:center;justify-content:center}
</style>
</head>
<body>

<header class="abs site-header">
  <a class="abs nav-link" style="left:150px">Films</a>
  <a class="abs nav-link" style="left:237px">Prices</a>
  <a class="abs nav-link" style="left:328px">Options</a>
  <div class="abs brand-mark"></div>
  <div class="abs brand">BDMR</div>
  <a class="abs nav-link" style="left:803px">Reviews</a>
  <a class="abs nav-link" style="left:908px">About</a>
  <a class="abs nav-link" style="left:1000px">Contact</a>
</header>

<section class="abs hero" role="img" aria-label="Bride and groom cutting a tiered wedding cake under a warm spotlight in a dark hall"></section>
<h1 class="abs hero-title script">Wedding Photography</h1>
<p class="abs hero-sub">North East, Uk &amp; Worldwide</p>
<a class="abs btn-explore">Explore</a>

<h2 class="abs section-title script" style="top:780px">Our Services</h2>

<div class="abs tile" style="left:150px;top:853px;width:287px;height:212px;background:radial-gradient(ellipse 70px 90px at 25% 35%,rgba(40,60,80,.8),rgba(0,0,0,0)),radial-gradient(ellipse 50px 110px at 88% 75%,rgba(20,20,20,.85),rgba(0,0,0,0)),linear-gradient(120deg,#7a8590,#d8cfc6 45%,#b9aea5 70%,#9c948d)" role="img" aria-label="Couple portrait for cinematic highlights film"><div class="tile-band">Cinematic Highlights Film</div></div>
<div class="abs tile" style="left:451px;top:853px;width:299px;height:198px;background:radial-gradient(ellipse 70px 90px at 55% 55%,rgba(90,70,80,.6),rgba(0,0,0,0)),linear-gradient(170deg,#c8a9b8,#e4d4db 40%,#b69aa6 70%,#e5d8dd)" role="img" aria-label="Soft pink retro style wedding scene"><div class="tile-band">Retro Video</div></div>
<div class="abs tile" style="left:763px;top:853px;width:287px;height:212px;background:radial-gradient(ellipse 60px 80px at 40% 80%,rgba(250,250,250,.9),rgba(0,0,0,0)),radial-gradient(ellipse 40px 70px at 70% 60%,rgba(40,40,40,.7),rgba(0,0,0,0)),linear-gradient(180deg,#707070,#b8b8b8 40%,#9a9a9a 70%,#505050)" role="img" aria-label="Black and white church ceremony"><div class="tile-band">Ceremony and Speeches</div></div>

<div class="abs tile" style="left:150px;top:1089px;width:287px;height:283px;background:radial-gradient(ellipse 70px 100px at 40% 60%,rgba(20,20,20,.9),rgba(0,0,0,0)),radial-gradient(ellipse 60px 60px at 10% 40%,rgba(110,150,80,.7),rgba(0,0,0,0)),linear-gradient(135deg,#e0e0dc,#f3f3f1 50%,#d0d0cc)" role="img" aria-label="Tablet and phone showing a personal video album"><div class="tile-band">Personal Video Album</div></div>
<div class="abs tile" style="left:451px;top:1067px;width:299px;height:299px;background:radial-gradient(ellipse 110px 140px at 55% 50%,rgba(232,200,180,.9),rgba(0,0,0,0)),radial-gradient(ellipse 60px 40px at 50% 20%,rgba(90,60,40,.5),rgba(0,0,0,0)),linear-gradient(160deg,#7c6050,#c9a48e 50%,#a88672)" role="img" aria-label="Close-up of a bride smiling"><div class="tile-band">Extended Documentary Film</div></div>
<div class="abs tile" style="left:763px;top:1082px;width:287px;height:284px;background:radial-gradient(ellipse 80px 110px at 35% 30%,rgba(240,215,180,.85),rgba(0,0,0,0)),radial-gradient(ellipse 90px 80px at 70% 80%,rgba(160,150,190,.8),rgba(0,0,0,0)),linear-gradient(150deg,#b3463a,#e3a798 45%,#c98880)" role="img" aria-label="Bride embracing a guest"><div class="tile-band">Social Media Films &amp; Stories</div></div>

<div class="abs tile" style="left:150px;top:1382px;width:287px;height:223px;background:radial-gradient(ellipse 90px 70px at 55% 30%,rgba(230,205,190,.9),rgba(0,0,0,0)),radial-gradient(ellipse 110px 70px at 60% 90%,rgba(70,90,130,.85),rgba(0,0,0,0)),linear-gradient(150deg,#8c7466,#c8b2a4 50%,#6a7890)" role="img" aria-label="Guest hugging with eyes closed"><div class="tile-band">Guest Messages</div></div>
<div class="abs tile" style="left:451px;top:1382px;width:599px;height:223px;background:radial-gradient(ellipse 70px 120px at 38% 60%,rgba(230,225,215,.9),rgba(0,0,0,0)),radial-gradient(ellipse 60px 120px at 20% 60%,rgba(25,35,55,.9),rgba(0,0,0,0)),linear-gradient(90deg,#2b3646,#55606a 30%,#8c8a80 45%,#242424 65%,#111)" role="img" aria-label="Bride and groom touching foreheads outdoors"><div class="tile-band">Our Story Feature</div></div>

<div class="abs hello script">Hello,<br>I'm Ben Marlow</div>
<p class="abs about-text">A wedding filmmaker based in the North East of England.<br>We film weddings in a fun and natural way. All weddings<br>are totally unique to the couple. If you are looking for a<br>wedding film for your special day we would love to<br>hear from you.</p>
<a class="abs btn-outline">More About Me</a>
<div class="abs about-frame"></div>
<div class="abs about-photo" role="img" aria-label="Filmmaker holding a camera seen through glass"></div>

<h2 class="abs section-title script" style="top:2330px">What They Say About Us</h2>

<div class="abs cell" style="left:150px;top:2409px;background:radial-gradient(ellipse 80px 120px at 70% 55%,rgba(220,190,175,.85),rgba(0,0,0,0)),linear-gradient(125deg,#ece9e6,#c9c2bb 45%,#1c2232 75%,#121620)" role="img" aria-label="Couple's hands showing wedding rings"></div>
<div class="abs cell" style="left:375px;top:2409px">
  <p class="quote">A huge thank you to you both, Ben and Owen, for being so amazing on our wedding day. You were both so friendly and approachable, which is exactly what people want on their wedding day. Your natural approach to filming was exactly what we wanted. We are over the moon with our wedding video, our highlights video is better than we could have ever imagined!</p>
  <div class="quote-name">HANNAH + OLIVER<br>Ashby Lodge</div>
</div>
<div class="abs cell" style="left:600px;top:2409px;background:radial-gradient(ellipse 70px 80px at 45% 30%,rgba(220,180,165,.8),rgba(0,0,0,0)),radial-gradient(ellipse 60px 70px at 60% 88%,rgba(215,175,160,.7),rgba(0,0,0,0)),linear-gradient(90deg,#e5dfd8,#f4f2ef 60%,#dfdcd6)" role="img" aria-label="Hands fastening the back of a wedding dress"></div>
<div class="abs cell" style="left:825px;top:2409px">
  <p class="quote">Ben was great along with Owen for our wedding. Very flexible and accommodating, not intrusive at all. Really calm characters who provided some laughs. Video ready by midday the following day even though Ben was still with us at 10.30pm! Fantastic! Really happy with the highlights video. Thanks so much!</p>
  <div class="quote-name">LUCY + DANIEL<br>Hillcrest Farm</div>
</div>

<div class="abs cell" style="left:150px;top:2804px">
  <p class="quote">Absolutely amazing videographer! What can we say, our short film captures our day perfectly and includes everything we wanted. Both Ben and Owen were most professional and easy to work with on the day. They captured moments that I wouldn't have seen otherwise (like groom panicking beforehand). Would highly recommend!</p>
  <div class="quote-name">AMY + THOMAS<br>North Brook Inn</div>
</div>
<div class="abs cell" style="left:375px;top:2804px;background:radial-gradient(ellipse 50px 60px at 40% 40%,rgba(60,45,40,.85),rgba(0,0,0,0)),radial-gradient(ellipse 60px 50px at 35% 62%,rgba(235,225,190,.9),rgba(0,0,0,0)),linear-gradient(160deg,#5e6264,#e8e9e6 40%,#d6d8d4 70%,#b4b0a6)" role="img" aria-label="Bride in a veil holding a bouquet"></div>
<div class="abs cell" style="left:600px;top:2804px">
  <p class="quote">One of the best decisions We made was choosing you guys to film our wedding! It's absolutely fantastic, it has everyone so emotional watching it, we can't thank you enough for capturing our special day! You were amazing from start to finish<br><br>Thanks so much.</p>
  <div class="quote-name">Megan and Samuel<br>Red Lion Elmford</div>
</div>
<div class="abs cell" style="left:825px;top:2804px;background:radial-gradient(ellipse 50px 130px at 22% 60%,rgba(245,240,230,.9),rgba(0,0,0,0)),radial-gradient(ellipse 80px 180px at 65% 70%,rgba(45,62,92,.95),rgba(0,0,0,0)),linear-gradient(180deg,#cfd7c9,#b9c2ae 35%,#8d9a7c 60%,#6f7a62)" role="img" aria-label="Bride and groom laughing outdoors"></div>

<footer class="abs footer"></footer>
<div class="abs foot-mark"></div>
<div class="abs foot-brand">BDMR</div>
<p class="abs foot-text" style="left:150px;top:3345px">Wedding Photography</p>
<p class="abs foot-text" style="left:150px;top:3367px">North East, UK and Worldwide</p>
<svg class="abs" style="left:150px;top:3397px" width="12" height="12" viewBox="0 0 12 12"><path d="M2 1l2.5 0 1 3-1.5 1a7 7 0 0 0 3 3l1-1.5 3 1V10a1 1 0 0 1-1 1A9 9 0 0 1 1 2a1 1 0 0 1 1-1z" fill="var(--gold)"/></svg>
<p class="abs foot-small" style="left:176px;top:3395px">01234 567 890</p>
<svg class="abs" style="left:150px;top:3422px" width="12" height="10" viewBox="0 0 12 10"><rect x="0.5" y="0.5" width="11" height="9" fill="none" stroke="var(--gold)"/><path d="M0.5 0.5l5.5 5 5.5-5" fill="none" stroke="var(--gold)"/></svg>
<p class="abs foot-small" style="left:176px;top:3419px">hello@bdmrfilms.com</p>

<p class="abs foot-head" style="left:526px;top:3312px">Quick Links</p>
<p class="abs foot-small" style="left:526px;top:3337px">Home</p>
<p class="abs foot-small" style="left:526px;top:3361px">Films</p>
<p class="abs foot-small" style="left:526px;top:3385px">Photos</p>
<p class="abs foot-small" style="left:526px;top:3409px">Retro Videos</p>
<p class="abs foot-small" style="left:526px;top:3433px">Love Stories</p>
<p class="abs foot-small" style="left:526px;top:3457px">Moments</p>
<p class="abs foot-small" style="left:634px;top:3339px">Prices</p>
<p class="abs foot-small" style="left:634px;top:3363px">Options</p>
<p class="abs foot-small" style="left:634px;top:3387px">Reviews</p>
<p class="abs foot-small" style="left:634px;top:3411px">Blog</p>
<p class="abs foot-small" style="left:634px;top:3435px">FAQs</p>
<p class="abs foot-small" style="left:634px;top:3459px">Contact</p>

<p class="abs foot-head" style="left:832px;top:3312px">Stay Updated</p>
<div class="abs social" style="left:829px;top:3344px"></div>
<div class="abs social" style="left:881px;top:3344px"></div>
<div class="abs social" style="left:933px;top:3344px"></div>
<div class="abs badge"></div>

<div class="abs legal">BDMR 2020 © All Rights Reserved.</div>

</body>
</html>
```